Book cover design for an inspirational book on "Velvendary" Living

Velvendary Dwelling is a phase I have coined to describe inspirational life principles that emerge by following your passion in life. My passion is shabby chic furniture and décor. I run an on-line business called Dearly Kept Goods - see my web site www.dearlykeptgoods.com.au and the links to my Chatterbook page (daily inspiration) and my ClipStream channel - Velvendary TV to get a fuller sense of my passion.

The Book is loosely modelled on the "Warm Bread for the Weary" formula with the exception all of the stories are my own. I tell stories about pieces of furniture that I have created and demonstrate essential life lessons and principles though those creations. Examples of the life lessons (to help illustrate) include the importance of living in the now, overcoming obstacles in life, following your passion and love. The vehicle to carry these messages is Shabby Chic - my passion.

The title of the book is Velvendary Dwelling - Worn Tales of Warmth, Drive and Uplift. The author is my partner - Mira Tolk. I was intending this to be an e-book in the first instance with an option to go to print.
Updates

please see new addition of pictures and writing preference in script ,                                    

instead of stories of passion and love, to replace with   Follow your passion and create from your heart , (symbol of heart) at the side of end ...maybe ..  

Finding and following  your passion

Target Market(s)

Women across a fairly broad spectrum of 20's to mid 60's.

People interested in "new age" in the sense of finding and following your life passion.

Positive energy and traditional principles of happy home, family and passion for living and life.

Industry/Entity Type

Business

Font styles to use
Script

Colors
eea4c8

Requirements
Must have
• The book is inspirational and heart warming so the design should carry a positive energy that catches the eye and invites the reader to open the book to find out more.
Nice to have
• A shabby chic feel and style. My favourite colour is pink and I adore roses but this is not mandatory. The current visitor profile to my Chatterbook and ClipStream sites is 85% female generally between the early 20's to the mid 60's in age.

I am more interested in classy and positive than "girly". I am aiming the book at both genders but realise the appeal will be greatest to women.
Should not have
• I am looking for unique so want to be different than say Odette Pruvin who is one of the leaders in the world of shabby chic. The book is from me, so whilst I have provided my logo, I don't think it needs to feature in the design necessarily.

```html
<!DOCTYPE html>
<html lang="en">
<head>
<meta charset="utf-8">
<title>Velvendary Dwelling – Book Cover</title>
<link rel="stylesheet" href="https://fonts.googleapis.com/css2?family=Big+Shoulders+Display:wght@200&family=Courgette&family=Libre+Baskerville&display=swap">
<style>
  :root {
    --paper: #ffffff;
    --title-magenta: #c21a80;
    --subtitle-plum: #561b4e;
    --band-orange: #f47f20;
    --bloom-gold: #f8c84a;
    --bloom-light: #fde6a0;
    --bloom-heart: #c98a3a;
    --author-white: #ffffff;
  }
  html, body {
    margin: 0;
    padding: 0;
    width: 800px;
    height: 1200px;
    overflow: hidden;
    background: var(--paper);
  }
  .cover {
    position: relative;
    width: 800px;
    height: 1200px;
    background: var(--paper);
    overflow: hidden;
  }
  .cover-bloom {
    position: absolute;
    left: 298px;
    top: 68px;
    width: 204px;
    height: 204px;
  }
  .book-title {
    position: absolute;
    left: 0;
    top: 348px;
    width: 800px;
    margin: 0;
    text-align: center;
    font-family: "Big Shoulders Display", "Arial Narrow", sans-serif;
    font-weight: 200;
    color: var(--title-magenta);
    text-transform: uppercase;
    font-size: 112px;
    line-height: 124px;
    letter-spacing: 0.26em;
  }
  .book-title span {
    display: block;
    padding-left: 0.26em;
  }
  .bloom-row {
    position: absolute;
    left: 300px;
    top: 658px;
    width: 200px;
    height: 46px;
  }
  .book-subtitle {
    position: absolute;
    left: 0;
    top: 722px;
    width: 800px;
    margin: 0;
    text-align: center;
    font-family: "Courgette", cursive;
    font-weight: 400;
    color: var(--subtitle-plum);
    font-size: 44px;
    line-height: 56px;
  }
  .author-band {
    position: absolute;
    left: 0;
    top: 980px;
    width: 800px;
    height: 220px;
  }
  .author-name {
    position: absolute;
    left: 56px;
    top: 1082px;
    margin: 0;
    font-family: "Libre Baskerville", Georgia, serif;
    font-weight: 400;
    font-size: 62px;
    line-height: 1;
    color: var(--author-white);
  }
</style>
</head>
<body>
  <main class="cover">
    <svg class="cover-bloom" viewBox="0 0 204 204" role="img" aria-label="Yellow daisy flower illustration">
      <defs>
        <radialGradient id="bloomTone" cx="50%" cy="50%" r="50%">
          <stop offset="0%" stop-color="var(--bloom-heart)"/>
          <stop offset="18%" stop-color="var(--bloom-gold)"/>
          <stop offset="100%" stop-color="var(--bloom-light)"/>
        </radialGradient>
      </defs>
      <circle cx="102" cy="102" r="100" fill="url(#bloomTone)"/>
    </svg>

    <h1 class="book-title">
      <span>Velvendary</span>
      <span>Dwelling</span>
    </h1>

    <svg class="bloom-row" viewBox="0 0 200 46" role="img" aria-label="Row of three small daisy ornaments">
      <defs>
        <radialGradient id="smallBloomTone" cx="50%" cy="50%" r="50%">
          <stop offset="0%" stop-color="var(--bloom-heart)"/>
          <stop offset="25%" stop-color="var(--bloom-gold)"/>
          <stop offset="100%" stop-color="var(--bloom-light)"/>
        </radialGradient>
      </defs>
      <circle cx="24" cy="23" r="22" fill="url(#smallBloomTone)"/>
      <circle cx="100" cy="23" r="22" fill="url(#smallBloomTone)"/>
      <circle cx="176" cy="23" r="22" fill="url(#smallBloomTone)"/>
    </svg>

    <p class="book-subtitle">Worn Tales of Warmth,<br>Drive and Uplift</p>

    <svg class="author-band" viewBox="0 0 800 220" preserveAspectRatio="none" aria-hidden="true">
      <path d="M0,16 C150,56 330,76 520,86 C650,92 740,100 800,112 L800,220 L0,220 Z" fill="var(--band-orange)"/>
    </svg>
    <p class="author-name">Mira Tolk</p>
  </main>
</body>
</html>
```